Harlow's Wiring (www.harlowswiring.example)

I own and operate a telecommunication business in Dallas, Texas. We specialize in Ethernet cabling , networking, wireless implementation, security camera (CCTV) installation, Home theater systems, Audio/Video installations, Lighting

i would like a full vehicle wrap for the Tarven Roadmaster T340 Cargo Van
i will attach our company logo PDF so it can be added as well.
I am looking for a modern, sleek logo with Bold letters. i want it to scream luxury service.
please emphasize " 5 star rated on Pindle and Brisk" somehow, include "QTC A+ Rated" and Or the QTC A+ logo which i will include a photo of it.
I will also attach ideas of the van designs i like from the internet. i am open to changing my business colors so feel free to suggest new logo design/colors.
No Cartoon characters or people in van design.
i would like for the van wrap to include a few key words similar to the "sure cord" Van design on each side of the van wrap. Keywords can be: Network wiring | Audio | Video | Surveillance | Wi-Fi

please include my phone number 555 014 2286
and my website Harlowswiring.example

Vehicle wrap company image Requirements:
Create or convert all layered files to RGB Color Mode in Adobe Photoshop CS3 or Adobe Illustrator CS3. Do not use CMYK Color Mode.

Assign Adobe RGB (1998) Color Profile to both bitmap and vector-formatted files.

Send vector files as true vector files.

A bitmap image such as a .JPG or .TIF file, saved as an .EPS/.AI file in a vector program, such as Adobe Illustrator, does not constitute as being true vector.

Design all layered files at actual print size at 72 dpi, with at least 6” of extra bleed beyond vehicle outline.

Supplied art files must be in high resolution. If you are unsure of the resolution of an image, play it safe and always go big! The higher the resolution in dots per inch (dpi) and the bigger the dimensions, the less chance of the image(s) will have of pixelation.

Do not resize art files down for uploading purposes. Instead, compress all files, individually

```html
<!DOCTYPE html>
<html lang="en">
<head>
<meta charset="utf-8">
<title>Harlow's Wiring – Van Wrap</title>
<link rel="stylesheet" href="https://fonts.googleapis.com/css2?family=Poppins:wght@500;600;700&display=swap">
<style>
  :root {
    --bg: #ffffff;
    --body: #2f2a27;
    --gold: #b08d57;
    --white: #e9e7e4;
    --glass: #9a9a9a;
    --tyre: #1c1c1c;
    --rim: #8f9499;
    --chrome: #bfc2c4;
    --lamp: #b3262a;
    --shadow: #111111;
    --badge: #2c6e9e;
  }
  html, body { margin: 0; padding: 0; overflow: hidden; background: var(--bg); }
  .canvas { width: 744px; height: 1200px; display: block; }
  .van-body { fill: var(--body); }
  .gold-band { fill: var(--gold); }
  .glass { fill: var(--glass); }
  .tyre { fill: var(--tyre); }
  .rim { fill: var(--rim); }
  .chrome { fill: var(--chrome); }
  .lamp { fill: var(--lamp); }
  .ground-shadow { fill: var(--shadow); }
  .mark-square { fill: none; stroke: var(--gold); }
  .badge-shape { fill: var(--badge); }
  .wordmark, .tagline, .phone, .keywords, .web, .rating {
    font-family: "Poppins", sans-serif;
  }
  .wordmark { fill: var(--white); font-weight: 600; }
  .tagline { fill: var(--white); font-weight: 500; }
  .phone { fill: var(--gold); font-weight: 700; }
  .keywords { fill: var(--gold); font-weight: 700; }
  .web { fill: var(--gold); font-weight: 600; }
  .rating { fill: var(--gold); font-weight: 700; }
</style>
</head>
<body>
<svg class="canvas" viewBox="0 0 744 1200" xmlns="http://www.w3.org/2000/svg">

  <!-- Driver side view -->
  <g class="view view-left">
    <ellipse class="ground-shadow" cx="370" cy="318" rx="318" ry="22"/>
    <rect class="chrome" x="48" y="252" width="45" height="26" rx="5"/>
    <rect class="chrome" x="665" y="260" width="32" height="26" rx="5"/>
    <path class="van-body" d="M60,205 Q66,186 95,180 L160,170 L236,110 Q248,102 272,101 L650,98 Q663,100 668,115 L680,190 L682,268 L670,292 L604,292 A46,46 0 0 0 512,292 L190,292 A46,46 0 0 0 98,292 L62,292 L58,262 Z"/>
    <path class="glass" d="M214,170 L243,120 L298,116 L296,176 L214,178 Z"/>
    <path class="gold-band" d="M470,99 L508,99 Q478,138 430,150 L190,196 L64,217 L62,207 L188,184 L424,137 Q452,128 470,99 Z"/>
    <path class="gold-band" d="M312,292 Q334,270 382,262 L680,216 L681,227 L392,274 Q362,281 350,292 Z"/>
    <rect class="lamp" x="668" y="200" width="10" height="36"/>
    <rect class="chrome" x="60" y="210" width="20" height="36" rx="3"/>
    <rect class="mark-square" x="528" y="112" width="104" height="104" rx="10" stroke-width="12"/>

    <text class="phone" x="322" y="146" font-size="19" transform="rotate(-7 322 146)">555 014 2286</text>
    <text class="wordmark" x="196" y="236" font-size="41" transform="rotate(-9.5 196 236)">HARLOW'S</text>
    <text class="tagline" x="275" y="258" font-size="24" letter-spacing="8" transform="rotate(-9.5 275 258)">WIRING</text>
    <text class="keywords" x="211" y="288" font-size="9.6" transform="rotate(-9.5 211 288)">NETWORK WIRING | AUDIO | VIDEO | SURVEILLANCE | WI-FI</text>
    <text class="web" x="88" y="222" font-size="8.5" transform="rotate(-9 88 222)">Harlowswiring.example</text>

    <text class="rating" x="614" y="262" font-size="10">Pindle</text>
    <text class="rating" x="616" y="272" font-size="6" letter-spacing="1">★★★★★</text>
    <rect class="badge-shape" x="652" y="246" width="18" height="24" rx="2"/>

    <circle class="tyre" cx="144" cy="298" r="46"/>
    <circle class="rim" cx="144" cy="298" r="36"/>
    <circle class="tyre" cx="144" cy="298" r="8"/>
    <circle class="tyre" cx="558" cy="298" r="46"/>
    <circle class="rim" cx="558" cy="298" r="36"/>
    <circle class="tyre" cx="558" cy="298" r="8"/>
  </g>

  <!-- Passenger side view -->
  <g class="view view-right">
    <g transform="translate(744,385) scale(-1,1)">
      <ellipse class="ground-shadow" cx="370" cy="318" rx="318" ry="22"/>
      <rect class="chrome" x="48" y="252" width="45" height="26" rx="5"/>
      <rect class="chrome" x="665" y="260" width="32" height="26" rx="5"/>
      <path class="van-body" d="M60,205 Q66,186 95,180 L160,170 L236,110 Q248,102 272,101 L650,98 Q663,100 668,115 L680,190 L682,268 L670,292 L604,292 A46,46 0 0 0 512,292 L190,292 A46,46 0 0 0 98,292 L62,292 L58,262 Z"/>
      <path class="glass" d="M214,170 L243,120 L298,116 L296,176 L214,178 Z"/>
      <path class="gold-band" d="M470,99 L508,99 Q478,138 430,150 L190,196 L64,217 L62,207 L188,184 L424,137 Q452,128 470,99 Z"/>
      <path class="gold-band" d="M312,292 Q334,270 382,262 L680,216 L681,227 L392,274 Q362,281 350,292 Z"/>
      <rect class="lamp" x="668" y="200" width="10" height="36"/>
      <rect class="chrome" x="60" y="210" width="20" height="36" rx="3"/>
      <rect class="mark-square" x="528" y="112" width="104" height="104" rx="10" stroke-width="12"/>
      <circle class="tyre" cx="144" cy="298" r="46"/>
      <circle class="rim" cx="144" cy="298" r="36"/>
      <circle class="tyre" cx="144" cy="298" r="8"/>
      <circle class="tyre" cx="558" cy="298" r="46"/>
      <circle class="rim" cx="558" cy="298" r="36"/>
      <circle class="tyre" cx="558" cy="298" r="8"/>
    </g>

    <text class="phone" x="308" y="510" font-size="19" transform="rotate(7 308 510)">555 014 2286</text>
    <text class="wordmark" x="250" y="567" font-size="41" transform="rotate(9.5 250 567)">HARLOW'S</text>
    <text class="tagline" x="318" y="616" font-size="24" letter-spacing="8" transform="rotate(9.5 318 616)">WIRING</text>
    <text class="keywords" x="243" y="620" font-size="9.6" transform="rotate(9.5 243 620)">NETWORK WIRING | AUDIO | VIDEO | SURVEILLANCE | WI-FI</text>
    <text class="web" x="656" y="612" font-size="8.5" text-anchor="end" transform="rotate(9 656 612)">Harlowswiring.example</text>

    <rect class="badge-shape" x="82" y="631" width="18" height="24" rx="2"/>
    <text class="rating" x="104" y="646" font-size="10">Pindle</text>
    <text class="rating" x="107" y="656" font-size="6" letter-spacing="1">★★★★★</text>
  </g>

  <!-- Rear view -->
  <g class="view view-rear">
    <ellipse class="ground-shadow" cx="372" cy="1118" rx="160" ry="12"/>
    <rect class="tyre" x="252" y="1060" width="34" height="56" rx="8"/>
    <rect class="tyre" x="462" y="1060" width="34" height="56" rx="8"/>
    <path class="van-body" d="M272,860 L480,856 L496,905 L504,1050 L244,1050 L250,905 Z"/>
    <rect class="lamp" x="246" y="962" width="20" height="42" rx="2"/>
    <rect class="lamp" x="484" y="962" width="20" height="42" rx="2"/>
    <rect class="lamp" x="358" y="852" width="34" height="4" rx="2"/>
    <rect class="tyre" x="388" y="974" width="60" height="28" rx="3"/>
    <rect class="gold-band" x="266" y="1005" width="218" height="7"/>
    <rect class="mark-square" x="357" y="868" width="38" height="38" rx="4" stroke-width="6"/>

    <text class="wordmark" x="375" y="935" font-size="21" text-anchor="middle">HARLOW'S</text>
    <text class="tagline" x="375" y="953" font-size="11" letter-spacing="4" text-anchor="middle">WIRING</text>
    <text class="keywords" x="375" y="966" font-size="5.2" text-anchor="middle">NETWORK WIRING | AUDIO | VIDEO | SURVEILLANCE | WI-FI</text>
    <text class="phone" x="274" y="998" font-size="15">555 014 2286</text>

    <rect class="badge-shape" x="316" y="1018" width="15" height="22" rx="2"/>
    <text class="rating" x="336" y="1032" font-size="9">Pindle</text>
    <text class="rating" x="340" y="1041" font-size="5" letter-spacing="1">★★★★★</text>

    <rect class="chrome" x="244" y="1050" width="262" height="14" rx="4"/>
  </g>
</svg>
</body>
</html>
```